Banner Ad Design for Bidmark

We are an online upscale fashion private sales site that requires banners in the following sizes and dimensions (see below). For submission, you can just submit three variations (letterheard, skyscrapper and square). The rest can be submitted later on when your design is selected. All banners can have the same look and feel or different if you feel so. They are going to be used in Plexo. So it's mandatory to abide by Plexo guidelines (Reminder given below). I have attached two files for your use, one is the company's logo and the other is one couple picture that you could use in the banner - You dont have to use them, they are material for your thoughts.

Creative Direction of Ad:
* Simple and not overly crowded
* Has a call to action (Join us, etc)
* Attention grabbing and conforms to an upscale fashion retailer (Chic & Stylish)
* Uses at least one of our unique selling proposition texts
* Informative and promotes only a visitor who is interested to click

Unique Selling Proposition:
* Private sales in Morocco
* Upscale fashion brands at -70%
* Exclusively in Morocco

IMPORTANT: Please make the banner in English but after the winner is selected, I will need the banner in French (I will provide you with the appropriate translation).

Sizes: (MAX 50K or smaller)
1. Square 250 x250
2. Small Square 200 x 189
3. Leaderboard 728 x 79
4. Sky scrapper 160x600
4. Medium Rectangle 300 x 250
5. Large Rectangle 336 x 280

(After the successful award, please also adapt the banner to add the following sizes
6. Leaderboard 468 x 60
7. Skyscrapper 120 x 600)

Winner will send the files in .Gif, JPEG, & PSD. If you have any questions, please dont hesitate to ask.

======================================================
Plexo Terms:
Ad images must be clear, recognizable, and relevant. Text appearing in the ad images must be legible. We reserve the right to disapprove low quality or blurry ad images.

Strobing, flashing backgrounds, or otherwise distracting ads are not allowed.
Your ads cannot mimic news articles and features. They may also not contain screenshots of Plexo BidLines text ads or otherwise simulate an BidLines text ad in any way.
Ads cannot pretend to be a system or site warning.
Ads cannot mimic or resemble Panels, Zed, or Orvo dialogue boxes, error message, etc.
Ads cannot have mock animated features or icons.
Ads can have an imaged button as long as the purpose of the message within the button is served or achieved through the landing page.
Specific for animated and display ad builder (template) ads:
Ads cannot have mock animated features or icons without the functionality working.

Target Market(s)

23-45 years white collard suburbans (Men & Women)

Industry/Entity Type

Fashion

Requirements
Must have
• Chic & Stylish Design.
It is not mandatory to use one of the logo file atatched but if you do not use it, please clearly display the site url (LUXE-CLUB.example)
Nice to have
• The couple picture attached but not necesarily if you have better design. I have provided two logos version (one with white and the other with black background. Use the one that suits your design best).

```html
<!DOCTYPE html>
<html lang="en">
<head>
<meta charset="utf-8">
<title>LUXE-CLUB.example — Banner Set</title>
<link href="https://fonts.googleapis.com/css2?family=Cinzel:wght@400;600&display=swap" rel="stylesheet">
<style>
  :root {
    --canvas: #000000;
    --panel-top: #232323;
    --panel-bottom: #3e3e3e;
    --gold: #e6b43c;
    --gold-light: #f3cc5c;
    --gold-dark: #c8941f;
    --ink: #1c1a16;
    --brand-ink: #f4f1ea;
    --photo-light: #e9e6df;
    --photo-mid: #9c9a95;
    --photo-dark: #4a4846;
  }
  * { box-sizing: border-box; margin: 0; padding: 0; }
  html, body {
    width: 1200px; height: 857px; overflow: hidden;
    background: var(--canvas);
    font-family: "Cinzel", "Times New Roman", serif;
  }
  .canvas { position: relative; width: 1200px; height: 857px; }
  .banner {
    position: absolute; overflow: hidden;
    background: linear-gradient(180deg, var(--panel-top) 0%, var(--panel-bottom) 100%);
  }
  .banner--skyscraper { left: 79px; top: 68px; width: 189px; height: 707px; }
  .banner--leaderboard { left: 291px; top: 68px; width: 856px; height: 93px;
    background: linear-gradient(90deg, var(--panel-top) 0%, var(--panel-bottom) 60%, var(--panel-top) 100%); }
  .banner--square { left: 291px; top: 178px; width: 294px; height: 295px; }

  .brand { position: absolute; display: flex; flex-direction: column; align-items: center; gap: 5px; }
  .brand__dot { width: 30px; height: 30px; border-radius: 50%; background: var(--gold); }
  .brand__name { color: var(--brand-ink); font-weight: 600; letter-spacing: 0.02em; white-space: nowrap; }

  .cta {
    position: absolute; display: flex; align-items: center; justify-content: center;
    background: linear-gradient(180deg, var(--gold-light) 0%, var(--gold) 55%, var(--gold-dark) 100%);
    color: var(--ink); border-radius: 5px; font-weight: 600; letter-spacing: 0.02em;
  }
  .photo {
    position: absolute;
    background: linear-gradient(160deg, var(--photo-mid) 0%, var(--photo-light) 45%, var(--photo-dark) 100%);
  }
  .swoosh { position: absolute; }

  /* skyscraper */
  .banner--skyscraper .brand { left: 0; width: 100%; top: 30px; }
  .banner--skyscraper .brand__dot { width: 44px; height: 44px; }
  .banner--skyscraper .brand__name { font-size: 14px; }
  .sky-headline {
    position: absolute; left: 0; width: 100%; top: 210px;
    text-align: center; color: var(--gold); font-size: 29px; line-height: 48px; font-weight: 400;
  }
  .banner--skyscraper .cta { left: 17px; top: 446px; width: 154px; height: 41px; font-size: 25px; }
  .banner--skyscraper .swoosh { left: 0; top: 505px; width: 189px; height: 110px; }
  .banner--skyscraper .photo { left: 0; top: 540px; width: 189px; height: 167px; }

  /* leaderboard */
  .banner--leaderboard .brand { left: 20px; top: 10px; width: 124px; gap: 4px; }
  .banner--leaderboard .brand__dot { width: 34px; height: 34px; }
  .banner--leaderboard .brand__name { font-size: 10.5px; }
  .board-headline {
    position: absolute; left: 150px; top: 0; height: 93px; display: flex; align-items: center;
    color: var(--gold); font-size: 22px; letter-spacing: 0.01em;
  }
  .banner--leaderboard .cta { left: 511px; top: 34px; width: 124px; height: 33px; font-size: 20px; }
  .banner--leaderboard .swoosh { left: 560px; top: 0; width: 296px; height: 93px; }
  .banner--leaderboard .photo { left: 650px; top: 0; width: 206px; height: 93px; }

  /* square */
  .banner--square .brand { left: 0; width: 100%; top: 12px; gap: 4px; }
  .banner--square .brand__dot { width: 38px; height: 38px; }
  .banner--square .brand__name { font-size: 13px; }
  .square-lead {
    position: absolute; left: 0; width: 100%; top: 86px; text-align: center;
    color: var(--gold); font-size: 17px;
  }
  .square-figure {
    position: absolute; left: 0; width: 100%; top: 100px; text-align: center;
    color: var(--gold); font-size: 54px; line-height: 64px;
  }
  .banner--square .swoosh { left: 0; top: 170px; width: 294px; height: 125px; }
  .banner--square .photo { left: 0; top: 160px; width: 294px; height: 135px; }
  .banner--square .cta { left: 67px; top: 244px; width: 153px; height: 39px; font-size: 24px; }
</style>
</head>
<body>
<main class="canvas">

  <section class="banner banner--skyscraper" aria-label="Skyscraper banner">
    <div class="brand">
      <span class="brand__dot"></span>
      <span class="brand__name">LUXE-CLUB.example</span>
    </div>
    <h2 class="sky-headline">Upscale<br>fashion<br>brands<br>at -70%</h2>
    <div class="cta">Join Us</div>
    <svg class="swoosh" viewBox="0 0 189 110" preserveAspectRatio="none" aria-hidden="true">
      <path d="M0 110 L0 80 C60 70 140 45 189 0 L189 110 Z" fill="var(--gold)"/>
    </svg>
    <div class="photo" role="img" aria-label="Stylish couple in white hats and sunglasses leaning on a vintage convertible" style="clip-path: polygon(0 25%, 55% 10%, 100% 0, 100% 100%, 0 100%);"></div>
  </section>

  <section class="banner banner--leaderboard" aria-label="Leaderboard banner">
    <div class="brand">
      <span class="brand__dot"></span>
      <span class="brand__name">LUXE-CLUB.example</span>
    </div>
    <h2 class="board-headline">Private sales in Morocco</h2>
    <div class="cta">Join Us</div>
    <svg class="swoosh" viewBox="0 0 296 93" preserveAspectRatio="none" aria-hidden="true">
      <path d="M0 93 C80 80 150 40 200 0 L296 0 L296 93 Z" fill="var(--gold)"/>
    </svg>
    <div class="photo" role="img" aria-label="Stylish couple in white hats and sunglasses leaning on a vintage convertible" style="clip-path: polygon(10% 100%, 20% 40%, 45% 0, 100% 0, 100% 100%);"></div>
  </section>

  <section class="banner banner--square" aria-label="Square banner">
    <div class="brand">
      <span class="brand__dot"></span>
      <span class="brand__name">LUXE-CLUB.example</span>
    </div>
    <p class="square-lead">Upscale fashion brands at</p>
    <p class="square-figure">70%</p>
    <svg class="swoosh" viewBox="0 0 294 125" preserveAspectRatio="none" aria-hidden="true">
      <path d="M0 125 L0 110 C110 90 220 50 294 0 L294 125 Z" fill="var(--gold)"/>
    </svg>
    <div class="photo" role="img" aria-label="Stylish couple in white hats and sunglasses leaning on a vintage convertible" style="clip-path: polygon(0 30%, 30% 10%, 60% 0, 80% 20%, 85% 100%, 0 100%);"></div>
    <div class="cta">Join Us</div>
  </section>

</main>
</body>
</html>
```